Re-design of an existing website

We are needing a redesign of http://www.corvane-pharmacy.com/. Same colour scheme and content. The design needs to be done using Zurb Foundation 5 with all SCSS included and setup accordingly.

Placeholder images may be used for now as photo's are in progress. Must be responsive and work on all device types.
Updates

PLEASE NOTE: The project manager is currently on holidays until the 6th of September, hopefully we will have a decision closer to this date but it may be a few days after.

Industry/Entity Type

Medical

Coding

Coded - Design and coding required

Number of Pages Required

3 page

Font styles to use
Sans Serif

Requirements
Must have
• Zurb Foundation 5

```html
<!DOCTYPE html>
<html lang="en">
<head>
<meta charset="utf-8">
<title>The Corvane Pharmacy</title>
<link href="https://fonts.googleapis.com/css2?family=Open+Sans:wght@400;600;700;800&display=swap" rel="stylesheet">
<style>
:root{
  --navy:#16298a;
  --blue:#2444b3;
  --blue-light:#3a5fcf;
  --ink:#222;
  --muted:#666;
  --line:#d5d8e0;
  --hero-a:#f1f1f1;
  --hero-b:#c9cdd3;
  --band:#e9eaec;
  --footer:#23262c;
  --footer-deep:#15171b;
  --white:#fff;
}
*{box-sizing:border-box;margin:0;padding:0}
html,body{width:773px;height:1200px;overflow:hidden}
body{font-family:"Open Sans",Arial,sans-serif;color:var(--ink);background:var(--white);position:relative;font-size:8px;line-height:1.35}
.abs{position:absolute}

/* header */
.site-header{left:0;top:0;width:773px;height:54px}
.brand{left:40px;top:6px;display:flex;align-items:center;gap:6px}
.brand-mark{width:22px;height:22px;border-radius:50%;background:var(--navy)}
.brand-name{font-weight:800;font-size:15px;color:var(--navy);line-height:1}
.brand-tag{left:68px;top:24px;font-size:6px;color:var(--muted)}
.top-nav{left:405px;top:0;display:flex;height:16px}
.top-nav a{display:block;padding:3px 9px;font-size:7px;font-weight:600;color:var(--white);background:var(--navy);text-decoration:none;border-right:1px solid var(--blue-light)}
.top-nav a.active{background:var(--blue-light)}
.phone{left:640px;top:24px;display:flex;align-items:center;gap:4px;font-weight:700;font-size:11px;color:var(--navy)}
.main-nav{left:0;top:54px;width:773px;height:18px;background:var(--navy);display:flex;padding-left:32px}
.main-nav a{color:var(--white);font-size:7px;font-weight:600;text-decoration:none;padding:4px 10px;border-right:1px solid var(--blue-light)}

/* hero */
.hero{left:0;top:76px;width:773px;height:298px;background:linear-gradient(180deg,var(--hero-a),var(--hero-b))}
.hero-photo{left:440px;top:0;width:333px;height:298px;background:linear-gradient(135deg,#e9d9cf,#c7b8ae 55%,#d8d2cc)}
.hero-title{left:35px;top:80px;width:370px;color:var(--white);font-weight:800;font-size:17px;line-height:1.25;text-shadow:0 1px 2px rgba(0,0,0,.35)}
.hero-dots{left:35px;top:240px;display:flex;gap:5px}
.hero-dots span{width:7px;height:7px;border-radius:50%;background:#9aa3b8}
.hero-dots span.on{background:var(--navy)}

/* services */
.services{left:0;top:382px;width:773px;height:180px;display:flex;justify-content:center;gap:65px}
.service{width:110px;text-align:center}
.service-icon{width:80px;height:80px;margin:8px auto 6px;border-radius:50%;background:var(--navy);border:5px solid #dfe3ee;box-shadow:0 0 0 2px var(--navy)}
.service h3{font-size:11px;font-weight:700;color:var(--ink);line-height:1.2}
.rule{left:40px;top:572px;width:693px;height:1px;background:var(--line)}

/* welcome */
.section-title{font-size:15px;font-weight:800;color:var(--ink);display:flex;align-items:center;gap:6px}
.section-title b{color:var(--navy)}
.section-title .bar{width:18px;height:12px;background:var(--navy);border-radius:2px 8px 2px 2px}
.welcome-title{left:40px;top:604px}
.badge{left:58px;top:645px;width:120px;height:120px;border-radius:50%;background:#e4e8f3;border:4px solid var(--navy)}
.welcome-text{left:200px;top:640px;width:290px;font-size:7.4px;color:var(--muted);text-align:justify}
.btn{display:inline-block;background:var(--navy);color:var(--white);font-size:7px;font-weight:700;padding:3px 9px;border-radius:2px}
.read-more{left:420px;top:722px}
.quick-title{left:515px;top:604px}
.quick-form{left:515px;top:640px;width:200px}
.field{height:14px;border:1px solid var(--line);font-size:6.5px;color:#999;padding:2px 4px;margin-bottom:5px}
.field.msg{height:26px}
.submit{margin-top:3px}

/* support band */
.support{left:0;top:805px;width:773px;height:80px;background:var(--band)}
.support h2{position:absolute;left:90px;top:22px;font-size:30px;font-weight:800;letter-spacing:1px;color:var(--ink)}
.support h2 b{color:var(--navy)}
.support-photo{left:510px;top:0;width:110px;height:80px;background:linear-gradient(180deg,#cfd2d8,#b4b9c2)}

/* news & testimonials */
.news-title{left:40px;top:908px}
.news-list{left:40px;top:936px;width:300px}
.news-item{display:flex;gap:8px;margin-bottom:7px}
.date{width:26px;height:26px;background:var(--navy);color:var(--white);font-size:6px;text-align:center;font-weight:700;line-height:1.1;padding-top:4px;flex:none}
.news-item h4{font-size:7.5px;font-weight:700;color:var(--navy)}
.news-item p{font-size:6.8px;color:var(--muted)}
.says-title{left:400px;top:908px}
.quote{left:400px;top:936px;width:333px;height:70px;border:1px solid var(--line);padding:10px 12px 0 26px;font-size:7px;color:var(--muted)}
.quote-mark{position:absolute;left:8px;top:4px;font-size:22px;font-weight:800;color:#c8cde0}
.author{left:410px;top:1014px;display:flex;align-items:center;gap:7px;font-size:7.5px;font-weight:700;color:var(--navy)}
.avatar{width:22px;height:22px;border-radius:50%;background:#b9bcc4}

/* footer */
.site-footer{left:0;top:1042px;width:773px;height:138px;background:var(--footer);color:#c9ccd3;padding:12px 40px 0;display:flex;gap:20px}
.site-footer section{flex:1}
.site-footer h5{font-size:11px;font-weight:600;color:var(--white);margin-bottom:7px}
.site-footer li{list-style:none;font-size:6.8px;line-height:1.5}
.site-footer li::before{content:"› ";color:var(--blue-light)}
.contact-row{display:flex;gap:6px;align-items:flex-start;font-size:6.8px;margin-bottom:6px}
.site-footer p{font-size:6.8px}
.site-footer strong{color:var(--white);font-size:6.8px;display:block;margin-top:4px}
.social{display:flex;align-items:center;gap:6px;font-size:7px;margin-bottom:4px}
.social i{width:12px;height:12px;background:var(--blue-light);display:block}
.copyright{left:0;top:1180px;width:773px;height:20px;background:var(--footer-deep);color:#9aa0ab;font-size:6.5px;text-align:center;padding-top:6px}
</style>
</head>
<body>

<header class="abs site-header">
  <div class="abs brand"><span class="brand-mark"></span><span class="brand-name">The Corvane Pharmacy</span></div>
  <div class="abs brand-tag">Specialist Services for Special People</div>
  <nav class="abs top-nav">
    <a class="active">Home</a><a>Brochures</a><a>Employment</a><a>Opening Hours and Directions</a><a>Contact Us</a>
  </nav>
  <div class="abs phone">
    <svg width="12" height="12" viewBox="0 0 24 24"><path fill="#16298a" d="M6.6 10.8a15 15 0 0 0 6.6 6.6l2.2-2.2a1 1 0 0 1 1-.25 11.4 11.4 0 0 0 3.6.57 1 1 0 0 1 1 1V20a1 1 0 0 1-1 1A17 17 0 0 1 3 4a1 1 0 0 1 1-1h3.5a1 1 0 0 1 1 1c0 1.25.2 2.45.57 3.57a1 1 0 0 1-.25 1z"/></svg>
    +61 (07) 5550 1820
  </div>
</header>
<nav class="abs main-nav">
  <a>Community Pharmacy</a><a>CPAP</a><a>HMR</a><a>Oncology Services</a><a>Home Nursing</a><a>Nutrition</a><a>Compounding</a><a>Surgical Supply</a>
</nav>

<section class="abs hero">
  <div class="abs hero-photo" role="img" aria-label="Photo of a smiling mother holding her baby"></div>
  <h1 class="abs hero-title">Lorem ipsum dolor sit amet, consectetuer adipiscing elit sed diam nonummy nibh euismod</h1>
  <div class="abs hero-dots"><span class="on"></span><span></span><span></span><span></span></div>
</section>

<section class="abs services">
  <div class="service"><div class="service-icon" role="img" aria-label="Oncology services icon"></div><h3>Oncology<br>Services</h3></div>
  <div class="service"><div class="service-icon" role="img" aria-label="Sleep apnoea icon"></div><h3>Sleep<br>Apnoea</h3></div>
  <div class="service"><div class="service-icon" role="img" aria-label="Pharmaceutical compounding icon"></div><h3>Pharmaceutical<br>Compounding</h3></div>
  <div class="service"><div class="service-icon" role="img" aria-label="Home nursing icon"></div><h3>Home<br>Nursing</h3></div>
</section>
<div class="abs rule"></div>

<h2 class="abs section-title welcome-title"><span class="bar"></span>Welcome To <b>Corvane Pharmacy</b></h2>
<div class="abs badge" role="img" aria-label="Quality care certification badge"></div>
<p class="abs welcome-text">Lorem ipsum dolor sit amet, consectetuer adipiscing elit, sed diam nonummy nibh euismod tincidunt ut laoreet dolore magna aliquam erat volutpat. Ut wisi enim ad minim veniam, quis nostrud exerci tation ullamcorper suscipit lobortis nisl ut aliquip ex ea commodo consequat. Duis autem vel eum iriure dolor in hendrerit in vulputate velit esse molestie consequat, vel illum dolore eu feugiat nulla facilisis at vero eros et accumsan et iusto odio dignissim qui blandit praesent luptatum zzril delenit augue duis dolore te feugait nulla facilisi.</p>
<span class="abs btn read-more">Read More ›</span>

<h2 class="abs section-title quick-title"><span class="bar"></span><b>Quick</b>&nbsp;Contact</h2>
<form class="abs quick-form">
  <div class="field">Name</div>
  <div class="field">Email</div>
  <div class="field">Phone</div>
  <div class="field msg">Message</div>
  <span class="btn submit">SUBMIT ›</span>
</form>

<section class="abs support">
  <h2>24/7 CLIENT <b>SUPPORT</b></h2>
  <div class="abs support-photo" role="img" aria-label="Photo of a support agent wearing a headset"></div>
</section>

<h2 class="abs section-title news-title">Latest <b>News</b></h2>
<div class="abs news-list">
  <article class="news-item"><div class="date">JUN<br>12</div><div><h4>Lorem ipsum dolor sit amet</h4><p>Lorem ipsum dolor sit amet, consectetuer adipiscing elit sed diam nonummy.</p></div></article>
  <article class="news-item"><div class="date">JUN<br>08</div><div><h4>Lorem ipsum dolor sit amet</h4><p>Lorem ipsum dolor sit amet, consectetuer adipiscing elit sed diam nonummy.</p></div></article>
  <article class="news-item"><div class="date">MAY<br>27</div><div><h4>Lorem ipsum dolor sit amet</h4><p>Lorem ipsum dolor sit amet, consectetuer adipiscing elit sed diam nonummy.</p></div></article>
</div>

<h2 class="abs section-title says-title">What Our <b>Customers Speak</b></h2>
<blockquote class="abs quote"><span class="quote-mark">“</span>Lorem ipsum dolor sit amet consectetuer adipiscing elit sed diam nonummy nibh euismod tincidunt ut laoreet dolore magna aliquam erat volutpat ut wisi enim.</blockquote>
<div class="abs author"><span class="avatar" role="img" aria-label="Customer portrait"></span>Mr Calum Foster</div>

<footer class="abs site-footer">
  <section>
    <h5>Quick Links</h5>
    <ul><li>Community Pharmacy</li><li>CPAP</li><li>HMR</li><li>Oncology Services</li><li>Home Nursing</li><li>Nutrition</li><li>Compounding</li><li>Surgical Supply</li></ul>
  </section>
  <section>
    <h5>Contact Us</h5>
    <div class="contact-row"><svg width="9" height="9" viewBox="0 0 24 24"><path fill="#3a5fcf" d="M12 2a7 7 0 0 0-7 7c0 5 7 13 7 13s7-8 7-13a7 7 0 0 0-7-7zm0 9.5A2.5 2.5 0 1 1 12 6.5a2.5 2.5 0 0 1 0 5z"/></svg><span>Level 2 Harlow Building, 14 Fenwick St,<br>Brookvale, QLD 4000</span></div>
    <div class="contact-row"><svg width="9" height="9" viewBox="0 0 24 24"><path fill="#3a5fcf" d="M6.6 10.8a15 15 0 0 0 6.6 6.6l2.2-2.2a1 1 0 0 1 1-.25 11.4 11.4 0 0 0 3.6.57 1 1 0 0 1 1 1V20a1 1 0 0 1-1 1A17 17 0 0 1 3 4a1 1 0 0 1 1-1h3.5a1 1 0 0 1 1 1c0 1.25.2 2.45.57 3.57a1 1 0 0 1-.25 1z"/></svg><span>+61 (07) 5550 1820</span></div>
    <div class="contact-row"><svg width="9" height="9" viewBox="0 0 24 24"><path fill="#3a5fcf" d="M2 5h20v14H2zm2 2v.5l8 5 8-5V7z"/></svg><span>hello@corvanepharmacy.com.au</span></div>
  </section>
  <section>
    <h5>Opening Hours</h5>
    <p>We are open every day of the year</p>
    <strong>Monday to Friday</strong><p>7.30am – 9.00pm</p>
    <strong>Saturday</strong><p>8.00am – 6.00pm</p>
    <strong>Sunday and Public Holidays</strong><p>9.00am – 6.00pm</p>
  </section>
  <section>
    <h5>Follow Us On</h5>
    <div class="social"><i></i>Friendpage</div>
    <div class="social"><i></i>Chirper</div>
    <div class="social"><i></i>ClipTube</div>
    <div class="social"><i></i>WorkLink</div>
  </section>
</footer>
<div class="abs copyright">© 2013 CorvanePharmacy. All Rights Reserved.</div>

</body>
</html>
```